Real Estate Business Cards

Looking for a clean, sharp and professional look for our Real Estate investment Fund that invests in Multi Family Apartment buildings.

Target Market(s)

Real Estate Fund

Industry/Entity Type

Real Estate

Contact Information for Business Card

Company Description: Real Estate Investment Fund
Company Name: RKW Holdings
Name: Marcus Olvane
Cell: (917) 482-0657
Email: marcus@rkwholdings-example.com
Website: www.rkwholdings-example.com
Address: 418, 9th Street, Brooklyn NY 11218

Colors

Designer to choose colors to be used in the design.

Requirements
Nice to have
• Colors to match logo

```html
<!DOCTYPE html>
<html lang="en">
<head>
<meta charset="utf-8">
<title>RKW Holdings — Business Card</title>
<link rel="stylesheet" href="https://fonts.googleapis.com/css2?family=Lato:wght@400&family=Raleway:wght@300;400;700&display=swap">
<style>
  :root {
    --ink: #222222;
    --charcoal: #3a3a3c;
    --sky: #00abec;
    --accent: #1ea5e3;
    --brand-blue: #1a6fae;
    --paper: #ffffff;
  }
  html, body {
    margin: 0;
    padding: 0;
    width: 1200px;
    height: 720px;
    overflow: hidden;
    background: var(--paper);
  }
  .card {
    position: relative;
    width: 1200px;
    height: 720px;
    background: var(--paper);
    font-family: "Lato", sans-serif;
    color: var(--ink);
  }
  .brand {
    position: absolute;
    left: 747px;
    top: 95px;
    width: 400px;
    text-align: center;
  }
  .brand-square {
    display: block;
    width: 62px;
    height: 62px;
    margin: 0 auto 44px;
    background: var(--brand-blue);
  }
  .brand-name {
    margin: 0;
    font-family: "Lato", sans-serif;
    font-weight: 400;
    font-size: 36px;
    letter-spacing: 1px;
    line-height: 1;
    color: var(--brand-blue);
  }
  .brand-tagline {
    margin: 20px 0 0;
    font-size: 24px;
    line-height: 1;
    color: var(--ink);
  }
  .person {
    position: absolute;
    left: 76px;
    top: 298px;
  }
  .person-name {
    margin: 0;
    font-family: "Raleway", sans-serif;
    font-weight: 400;
    font-size: 43px;
    line-height: 1;
    color: var(--ink);
  }
  .person-name strong { font-weight: 700; }
  .person-role {
    margin: 12px 0 0;
    font-family: "Raleway", sans-serif;
    font-weight: 400;
    font-size: 24px;
    line-height: 1;
    color: var(--accent);
  }
  .rule {
    position: absolute;
    left: 265px;
    top: 363px;
    width: 935px;
    height: 4px;
    background: var(--charcoal);
  }
  .contacts {
    position: absolute;
    left: 85px;
    top: 464px;
    margin: 0;
    padding: 0;
    list-style: none;
  }
  .contacts li {
    display: flex;
    align-items: center;
    height: 36px;
    font-size: 24px;
  }
  .contacts svg {
    width: 26px;
    height: 26px;
    margin-right: 30px;
    fill: var(--accent);
    flex: none;
  }
  .address {
    position: absolute;
    right: 80px;
    top: 510px;
    margin: 0;
    font-style: normal;
    font-size: 24px;
    line-height: 33px;
    text-align: right;
  }
  .band {
    position: absolute;
    top: 622px;
    height: 80px;
  }
  .band-dark { left: 0; width: 593px; background: var(--charcoal); }
  .band-sky { left: 607px; width: 593px; background: var(--sky); }
</style>
</head>
<body>
<div class="card">
  <div class="brand">
    <span class="brand-square" aria-hidden="true"></span>
    <p class="brand-name">RKW HOLDINGS</p>
    <p class="brand-tagline">Real Estate Investment Fund</p>
  </div>

  <div class="person">
    <h1 class="person-name"><strong>MARCUS</strong> OLVANE</h1>
    <p class="person-role">Designation</p>
  </div>

  <div class="rule"></div>

  <ul class="contacts">
    <li>
      <svg viewBox="0 0 26 26" aria-hidden="true"><path d="M2 9c0-3 5-5 11-5s11 2 11 5v2h-6V8.5c-1.5-.6-3.3-.9-5-.9s-3.5.3-5 .9V11H2z"/><path d="M6 12h14l3 10H3z"/><circle cx="13" cy="17" r="3" fill="#fff"/></svg>
      (917) 482-0657
    </li>
    <li>
      <svg viewBox="0 0 26 26" aria-hidden="true"><path d="M1 4h24v18H1z"/><path d="M2 5l11 9 11-9" fill="none" stroke="#fff" stroke-width="1.8"/></svg>
      marcus@rkwholdings-example.com
    </li>
    <li>
      <svg viewBox="0 0 26 26" aria-hidden="true"><circle cx="13" cy="13" r="12"/><g fill="none" stroke="#fff" stroke-width="1.5"><ellipse cx="13" cy="13" rx="5" ry="12"/><path d="M13 1v24M1 13h24M3 7h20M3 19h20"/></g></svg>
      www.rkwholdings-example.com
    </li>
  </ul>

  <address class="address">418, 9th Street,<br>Brooklyn NY 11218</address>

  <div class="band band-dark"></div>
  <div class="band band-sky"></div>
</div>
</body>
</html>
```